QRV Stationery Design Project

Dear Designers,
We need a new stationery design for company to match our new logo.
Designers should provide a design for the following:
1. Business Card: 3.5x2 Inches.
2. Letterhead: A4 size.
3. Envelops: 25x35.5 Cm.
You can keep the Arabic name at the bottom of the logo Or you can use the separate attached Arabic Name.
Please refer to the attached logo guide for design information.
Sample Business Card information:
Name: Tariq Nawaf
Position: Operation Manager
Tel: +966 920007714 Ex. 500
Fax: +966 (3)8842617
Mob: +966 (5)00387251
email: tariq@qrv-example.com.sa
URL: www.qrv-example.com.sa
Address:
Al Wadi Tower, Suite 303
Nasser bin Salem Str.
Khobar, 31847
Saudi Arabia
Updates
Dear All,
Please note, we had uploaded our logo along with Arabic writing in Adobe illustrator format (.ai).
Regards,
Khalid
Dear All,
A sample data for the business card had been added as per your request.
Regards,
Khalid

```html
<!DOCTYPE html>
<html lang="en">
<head>
<meta charset="utf-8">
<title>QRV Business Card</title>
<link rel="stylesheet" href="https://fonts.googleapis.com/css2?family=Exo+2:wght@700&family=Arimo:wght@400;700&display=swap">
<style>
  :root {
    --navy: #1f3a68;
    --grey: #a9abae;
    --grey-light: #c9cacc;
    --white: #ffffff;
    --backdrop: #e6e7e9;
  }
  * { box-sizing: border-box; margin: 0; padding: 0; }
  html, body { width: 1067px; height: 1200px; overflow: hidden; }
  body {
    background: var(--backdrop);
    font-family: "Arimo", Arial, sans-serif;
    position: relative;
  }
  .card {
    position: absolute;
    left: 183px;
    width: 700px;
    height: 400px;
    overflow: hidden;
    box-shadow: 0 6px 18px rgba(0,0,0,.18);
  }
  .card--front { top: 90px; background: var(--navy); }
  .card--back  { top: 690px; background: var(--white); }

  .brand {
    display: flex; align-items: center; gap: 14px;
    font-family: "Exo 2", sans-serif; font-weight: 700;
    line-height: 1;
  }
  .brand__mark { flex: none; border-radius: 50%; }

  .card--front .brand {
    position: absolute; inset: 0; justify-content: center;
    color: var(--white); font-size: 92px; letter-spacing: 6px;
  }
  .card--front .brand__mark { background: var(--white); width: 24px; height: 24px; }

  .card--back .brand {
    position: absolute; left: 56px; top: 84px;
    color: var(--navy); font-size: 50px; letter-spacing: 3px;
  }
  .card--back .brand__mark { background: var(--navy); width: 18px; height: 18px; }

  .corner-steps { position: absolute; right: 0; top: 0; }

  .person { position: absolute; right: 96px; top: 50px; text-align: right; }
  .person__name {
    font-family: "Exo 2", sans-serif; font-weight: 700;
    font-size: 27px; line-height: 32px; color: var(--navy);
  }
  .person__role { font-size: 14px; line-height: 18px; color: var(--grey); }

  .contact {
    position: absolute; left: 330px; top: 168px;
    font-size: 13px; line-height: 18px; color: var(--navy); white-space: nowrap;
  }
  .contact__label { color: var(--grey); }

  .address {
    position: absolute; left: 60px; top: 218px;
    font-size: 13px; line-height: 17px; color: var(--navy); font-style: normal; white-space: nowrap;
  }

  .footer-art { position: absolute; left: 0; bottom: 0; }
  .website {
    position: absolute; left: 64px; bottom: 32px;
    font-size: 15px; line-height: 18px; font-weight: 700; letter-spacing: 5px; color: var(--white);
    white-space: nowrap;
  }
</style>
</head>
<body>

<section class="card card--front" aria-label="Business card front">
  <div class="brand"><span class="brand__mark"></span>QRV</div>
</section>

<section class="card card--back" aria-label="Business card back">
  <div class="brand"><span class="brand__mark"></span>QRV</div>

  <svg class="corner-steps" width="90" height="110" viewBox="0 0 90 110" aria-hidden="true">
    <polygon points="20,20 48,20 48,50 20,40" fill="var(--grey-light)"/>
    <polygon points="54,30 90,30 90,78 54,66" fill="var(--grey-light)"/>
  </svg>

  <div class="person">
    <div class="person__name">Tariq Nawaf</div>
    <div class="person__role">Operation Manager</div>
  </div>

  <div class="contact">
    <div><span class="contact__label">Tel:</span> +966 920007714 Ex. 500</div>
    <div><span class="contact__label">Fax:</span> +966 (3)8842617</div>
    <div><span class="contact__label">Mob:</span> +966 (5)00387251</div>
    <div><span class="contact__label">Email:</span> tariq@qrv-example.com.sa</div>
  </div>

  <address class="address">
    Al Wadi Tower, Suite 303<br>
    Nasser bin Salem Str.<br>
    Khobar, 31847<br>
    Saudi Arabia
  </address>

  <svg class="footer-art" width="700" height="170" viewBox="0 0 700 170" aria-hidden="true">
    <polygon points="0,82 520,40 480,170 0,170" fill="var(--grey)"/>
  </svg>
  <svg class="footer-art" width="700" height="170" viewBox="0 0 700 170" role="img" aria-label="Vehicle illustration area in navy">
    <polygon points="520,40 700,10 700,170 480,170" fill="var(--navy)"/>
  </svg>

  <div class="website">www.qrv-example.com.sa</div>
</section>

</body>
</html>
```